Project Manager Business Card for Top Architectural Firm

Update and design a stunning Senior Project Manager Business Card

MARCO T. DRUMMOND II
Senior Project Manager

H A L C Y O N
A R C H I T E C T U R E L L C.
www.HalcyonGrandEstates.example
4127 NW 52nd Ter. Suite 2308
Miami, FL 33148
C: (305) 555-0184
mdrummond.halcyongrandestates@mailbox.example

Looking to have the logo to be UV Spot ink printed and to be prominent.

Target Market(s)

High end real estate architecture construction

Industry/Entity Type

Architect

Contact Information for Business Card

MARCO T. DRUMMOND II
Senior Project Manager

H A L C Y O N
Miami, FL 33148
C: (305) 555-0184

Font styles to use
Sans Serif

Colors

Designer to choose colors to be used in the design.

Requirements
Must have
• Prominent Logo

```html
<!DOCTYPE html>
<html lang="en">
<head>
<meta charset="utf-8">
<title>Halcyon Architecture – Business Card</title>
<link rel="stylesheet" href="https://fonts.googleapis.com/css2?family=Roboto+Condensed:wght@300;400;700&display=swap">
<style>
  :root {
    --stage: #e9e7e3;
    --card: #ffffff;
    --card-back: #2e6d8e;
    --name-blue: #2c6d9c;
    --title-orange: #e98447;
    --text-grey: #5a5a5a;
    --mark-ink: #2a2a2a;
    --mark-dot: #2f8fc4;
    --icon-navy: #24507a;
    --icon-red: #c8473a;
    --icon-blue: #2f8fc4;
  }
  * { margin: 0; padding: 0; box-sizing: border-box; }
  html, body { width: 1200px; height: 950px; overflow: hidden; }
  body {
    background: var(--stage);
    font-family: "Roboto Condensed", Arial, sans-serif;
    display: flex; flex-direction: column; align-items: center; justify-content: center;
    gap: 50px;
  }
  .card {
    width: 700px; height: 400px; border-radius: 22px;
    position: relative; box-shadow: 0 10px 30px rgba(0,0,0,.18);
  }
  .card--front { background: var(--card); }
  .card--back { background: var(--card-back); }

  .brand {
    position: absolute; top: 52px; right: 56px;
    display: flex; align-items: center; gap: 18px;
  }
  .brand__dot { width: 58px; height: 58px; border-radius: 50%; background: var(--mark-dot); }
  .brand__words { color: var(--mark-ink); font-weight: 300; line-height: 1; }
  .brand__name { font-size: 46px; letter-spacing: 0.02em; white-space: pre; }
  .brand__sub { font-size: 11.5px; margin-top: 8px; letter-spacing: 0.05em; white-space: pre; }

  .contact { position: absolute; left: 50px; bottom: 46px; color: var(--text-grey); }
  .contact__name { color: var(--name-blue); font-weight: 700; font-size: 24px; letter-spacing: .01em; }
  .contact__title { color: var(--title-orange); font-size: 18px; text-transform: uppercase; letter-spacing: .02em; margin-top: 2px; }
  .contact__address { font-size: 15.5px; line-height: 1.35; margin-top: 6px; }
  .contact__lines { list-style: none; margin-top: 8px; font-size: 15.5px; line-height: 1.45; }
  .contact__lines li { display: flex; align-items: center; gap: 8px; }
  .icon { width: 15px; height: 15px; flex: none; }
</style>
</head>
<body>
  <section class="card card--front">
    <div class="brand">
      <span class="brand__dot"></span>
      <div class="brand__words">
        <div class="brand__name">H A L C Y O N</div>
        <div class="brand__sub">A R C H I T E C T U R E  L L C.</div>
      </div>
    </div>

    <div class="contact">
      <h1 class="contact__name">MARCO T. DRUMMOND II</h1>
      <p class="contact__title">Senior Project Manager</p>
      <p class="contact__address">4127 NW 52nd Ter. Suite 2308<br>Miami, FL 33148</p>
      <ul class="contact__lines">
        <li>
          <svg class="icon" viewBox="0 0 16 16"><circle cx="8" cy="8" r="8" fill="var(--icon-navy)"/><rect x="5.5" y="3.5" width="5" height="9" rx="1" fill="#fff"/><rect x="6.5" y="4.8" width="3" height="5.5" fill="var(--icon-navy)"/></svg>
          (305) 555-0184
        </li>
        <li>
          <svg class="icon" viewBox="0 0 16 16"><circle cx="8" cy="8" r="8" fill="var(--icon-red)"/><rect x="4" y="5" width="8" height="6" fill="#fff"/><path d="M4 5 L8 8.5 L12 5" fill="none" stroke="var(--icon-red)" stroke-width="1"/></svg>
          mdrummond.halcyongrandestates@mailbox.example
        </li>
        <li>
          <svg class="icon" viewBox="0 0 16 16"><circle cx="8" cy="8" r="8" fill="var(--icon-blue)"/><circle cx="8" cy="8" r="4.2" fill="none" stroke="#fff" stroke-width="1"/><ellipse cx="8" cy="8" rx="1.8" ry="4.2" fill="none" stroke="#fff" stroke-width="1"/><line x1="3.8" y1="8" x2="12.2" y2="8" stroke="#fff" stroke-width="1"/></svg>
          www.HalcyonGrandEstates.example
        </li>
      </ul>
    </div>
  </section>

  <section class="card card--back" aria-label="Card reverse"></section>
</body>
</html>
```